Modern design for a watersports website

Building a brand new site for Kiteboarders/Kitesurfers .... this is the first of 8 sites we're rolling out.

We're as much looking for a partner to work with, and they will be chosen based on the winner of this site design.

It will need these menu pages:

1) How-To
2) Classifieds
3) Groups
4) News
5) Events

Width: 1150px

The home page, should feature:

1) A search box to enter a location
2) Under that, a series of boxes showing up to 5 previous locations chosen - these should be "buttons", directly under the location (i.e. no photo, just the location name)
3) Under that, a 5 x 3 grid of adverts, featuring a photo, a title & a price
4) Under that, top 5 headlines, each one featuring photo, headline & Summary
5) Under that, top 10 Group topics: Group, Title, Author, #Replies (no photo for these)
6) Under that, 5 x 3 grid of photos
7) Footer

Colours should be of the ocean:
Blues, greens, compatible with yellow. (i.e. not washed out blues like tellora), vibrant blues, but not too vivid as to overpower.

Avoid: Photos of any equipment, as they will date quickly.

Building

1 page

Sans Serif

• Ocean colours; blues
• Modern design

```html
<!DOCTYPE html>
<html lang="en">
<head>
<meta charset="utf-8">
<title>Tidewind – Kiteboarding Home</title>
<link href="https://fonts.googleapis.com/css2?family=Raleway:wght@400;500;600;700&family=Open+Sans:wght@400;600&display=swap" rel="stylesheet">
<style>
  :root{
    --orange:#f39200;
    --orange-light:#f7a51e;
    --blue:#1f87d8;
    --blue-dark:#1a6fc0;
    --sky:#5fb4ee;
    --sea:#2f88e3;
    --green:#6cae0a;
    --green-light:#8cc70f;
    --green-dark:#4f9a06;
    --ink:#333a40;
    --grey:#8a9096;
    --white:#ffffff;
  }
  *{box-sizing:border-box;margin:0;padding:0}
  html,body{width:1200px;height:2590px;overflow:hidden;background:var(--white)}
  body{font-family:"Open Sans",Arial,sans-serif;color:var(--ink);position:relative}
  .wrap{width:924px;margin:0 auto}

  /* header */
  .site-header{height:90px;display:flex;align-items:center;justify-content:space-between;padding:0 130px 0 138px}
  .brand{font-family:"Raleway",sans-serif;font-weight:700;font-size:28px;color:var(--blue);letter-spacing:.5px}
  .main-nav{display:flex;gap:38px;font-family:"Raleway",sans-serif;font-size:15.5px;font-weight:500;color:var(--ink)}

  /* hero */
  .hero{position:relative;height:468px;overflow:hidden}
  .hero-photo{position:absolute;inset:0;background:linear-gradient(180deg,#bcd6e6 0%,#7fb0cf 25%,#3d87b4 55%,#9fc6dc 80%,#e6f0f5 100%)}
  .hero-arrow{position:absolute;top:280px}
  .hero-arrow.prev{left:118px}
  .hero-arrow.next{right:128px}
  .location-box{position:absolute;left:345px;top:140px;width:524px;height:160px;background:linear-gradient(180deg,var(--orange-light),var(--orange));padding:22px 32px 0}
  .location-box h1{font-family:"Raleway",sans-serif;font-weight:600;font-size:24px;color:var(--white);letter-spacing:.3px}
  .location-box .lead{font-family:"Raleway",sans-serif;font-size:13px;color:var(--white);margin-top:2px}
  .search{margin-top:12px;height:32px;background:var(--white);display:flex;align-items:center;justify-content:space-between;padding:0 12px;font-size:11px;color:var(--grey)}
  .recent{margin-top:12px;font-family:"Raleway",sans-serif;font-size:13.5px;color:var(--white);display:flex;gap:10px}
  .recent .sep{opacity:.85}

  /* section titles */
  .section-title{font-family:"Raleway",sans-serif;font-weight:500;font-size:23px;text-align:center;letter-spacing:.3px}

  /* adverts */
  .adverts{padding-top:42px;height:668px}
  .adverts .section-title{color:var(--orange)}
  .advert-grid{display:grid;grid-template-columns:repeat(5,178px);column-gap:9px;row-gap:0;margin-top:28px}
  .advert{height:177px}
  .advert .photo{height:83px}
  .advert h3{font-family:"Raleway",sans-serif;font-weight:500;font-size:13.5px;margin-top:7px;color:var(--ink)}
  .advert p{font-size:10.5px;color:var(--grey);margin-top:1px}
  .advert .price{font-family:"Raleway",sans-serif;font-size:15px;color:var(--blue);margin-top:5px}

  /* events */
  .events{height:349px;background:linear-gradient(180deg,var(--sky),var(--sea));padding-top:50px}
  .events .section-title{color:var(--white)}
  .event-grid{display:grid;grid-template-columns:repeat(5,178px);column-gap:9px;margin-top:22px}
  .event .photo{height:95px;border:3px solid var(--white)}
  .event h3{font-family:"Raleway",sans-serif;font-weight:600;font-size:14px;color:var(--white);margin-top:8px}
  .event p{font-size:10px;line-height:1.55;color:#eaf4fd;margin-top:3px}

  /* groups */
  .groups{height:406px;padding-top:46px}
  .groups .section-title{color:var(--green)}
  .group-grid{display:grid;grid-template-columns:repeat(5,178px);column-gap:9px;row-gap:40px;margin-top:38px;padding-left:10px}
  .topic h3{font-family:"Raleway",sans-serif;font-weight:600;font-size:13.5px;color:var(--blue-dark)}
  .topic .group-name{font-family:"Raleway",sans-serif;font-weight:700;font-size:12px;color:var(--orange)}
  .topic p{font-size:9.5px;line-height:1.55;color:var(--grey);margin-top:3px}
  .topic .meta{font-size:9.5px;color:var(--ink);margin-top:5px;display:flex;align-items:center;gap:6px}
  .topic .meta span{display:inline-flex;align-items:center;gap:3px}

  /* gallery */
  .gallery{position:relative;height:497px;background:linear-gradient(180deg,var(--green-light),var(--green-dark));padding-top:40px}
  .gallery .notch{position:absolute;left:50%;top:0;transform:translateX(-50%)}
  .gallery .section-title{color:var(--white)}
  .photo-grid{display:grid;grid-template-columns:repeat(5,178px);column-gap:9px;row-gap:18px;margin-top:26px}
  .photo-grid .photo{height:106px;border:3px solid var(--white)}

  /* footer */
  .site-footer{height:112px;padding-top:36px}
  .site-footer .wrap{display:flex;justify-content:space-between}
  .footer-nav{font-family:"Raleway",sans-serif;font-size:14.5px;color:var(--ink);display:flex;gap:9px}
  .copyright{font-size:10px;color:var(--grey);margin-top:9px}
  .social{display:flex;gap:10px;font-family:"Raleway",sans-serif;font-weight:600;font-size:13px;color:var(--blue-dark)}

  /* photo tones */
  .t-ocean{background:linear-gradient(160deg,#3f78b8,#173f7c)}
  .t-spray{background:linear-gradient(160deg,#d6e2ea,#7d97ab)}
  .t-grey{background:linear-gradient(160deg,#8e9396,#4d5356)}
  .t-sky{background:linear-gradient(180deg,#9ac4e6,#3f83c4)}
  .t-dusk{background:linear-gradient(160deg,#b9c2c9,#333)}
  .t-beach{background:linear-gradient(180deg,#c8d6df,#8f9a8a)}
  .t-turq{background:linear-gradient(180deg,#8fd0e6,#2aa0c7)}
  .t-sunset{background:linear-gradient(180deg,#f2c45a,#d9871d)}
  .t-warm{background:linear-gradient(180deg,#d9b27c,#8c6a46)}
  .t-dark{background:linear-gradient(160deg,#6c5a4a,#1f1a16)}
</style>
</head>
<body>

<header class="site-header">
  <div class="brand">TIDEWIND</div>
  <nav class="main-nav">
    <span>Home</span><span>How-To, Classifieds</span><span>Groups</span><span>News</span><span>Events</span>
  </nav>
</header>

<section class="hero">
  <div class="hero-photo" role="img" aria-label="Kiteboarder riding across bright ocean spray"></div>
  <svg class="hero-arrow prev" width="24" height="52" viewBox="0 0 24 52"><polyline points="22,2 3,26 22,50" fill="none" stroke="#1a4f9a" stroke-width="2"/></svg>
  <svg class="hero-arrow next" width="24" height="52" viewBox="0 0 24 52"><polyline points="2,2 21,26 2,50" fill="none" stroke="#1a4f9a" stroke-width="2"/></svg>
  <div class="location-box">
    <h1>ENTER YOUR LOCATION</h1>
    <p class="lead">Mauris vel lacus vitae felis vestibulum volutpat Etiam est nunc venenatis</p>
    <div class="search">
      <span>Enter Your Location area</span>
      <svg width="16" height="16" viewBox="0 0 16 16"><circle cx="6.5" cy="6.5" r="5" fill="none" stroke="#c4c4c4" stroke-width="2"/><line x1="10.5" y1="10.5" x2="15" y2="15" stroke="#c4c4c4" stroke-width="2.4"/></svg>
    </div>
    <div class="recent">
      <span>Previous Locations:</span><span>Flo</span><span class="sep">|</span><span>Miami</span><span class="sep">|</span><span>Dallas</span><span class="sep">|</span><span>Austin</span><span class="sep">|</span><span>Detroit</span>
    </div>
  </div>
</section>

<section class="adverts">
  <h2 class="section-title">Latest Adverts</h2>
  <div class="wrap advert-grid">
    <article class="advert"><div class="photo t-ocean" role="img" aria-label="Kiteboarder jumping over dark water"></div><h3>Tittle goes here</h3><p>Pede Fusce tellus Sed metus augu</p><div class="price">$125.99</div></article>
    <article class="advert"><div class="photo t-grey" role="img" aria-label="Rider carving through waves"></div><h3>Tittle goes here</h3><p>Pede Fusce tellus Sed metus augu</p><div class="price">$125.99</div></article>
    <article class="advert"><div class="photo t-grey" role="img" aria-label="Board cutting through grey water"></div><h3>Tittle goes here</h3><p>Pede Fusce tellus Sed metus augu</p><div class="price">$125.99</div></article>
    <article class="advert"><div class="photo t-dusk" role="img" aria-label="Kitesurfer under a cloudy sky"></div><h3>Tittle goes here</h3><p>Pede Fusce tellus Sed metus augu</p><div class="price">$125.99</div></article>
    <article class="advert"><div class="photo t-dark" role="img" aria-label="Rider airborne at sunset"></div><h3>Tittle goes here</h3><p>Pede Fusce tellus Sed metus augu</p><div class="price">$125.99</div></article>

    <article class="advert"><div class="photo t-beach" role="img" aria-label="Crowd of riders on the beach"></div><h3>Tittle goes here</h3><p>Pede Fusce tellus Sed metus augu</p><div class="price">$125.99</div></article>
    <article class="advert"><div class="photo t-grey" role="img" aria-label="Kiteboarder jumping high"></div><h3>Tittle goes here</h3><p>Pede Fusce tellus Sed metus augu</p><div class="price">$125.99</div></article>
    <article class="advert"><div class="photo t-warm" role="img" aria-label="Rider on the shoreline"></div><h3>Tittle goes here</h3><p>Pede Fusce tellus Sed metus augu</p><div class="price">$125.99</div></article>
    <article class="advert"><div class="photo t-sky" role="img" aria-label="Kitesurfer in white spray"></div><h3>Tittle goes here</h3><p>Pede Fusce tellus Sed metus augu</p><div class="price">$125.99</div></article>
    <article class="advert"><div class="photo t-sky" role="img" aria-label="Kite against blue sky"></div><h3>Tittle goes here</h3><p>Pede Fusce tellus Sed metus augu</p><div class="price">$125.99</div></article>

    <article class="advert"><div class="photo t-turq" role="img" aria-label="Rider on turquoise water"></div><h3>Tittle goes here</h3><p>Pede Fusce tellus Sed metus augu</p><div class="price">$125.99</div></article>
    <article class="advert"><div class="photo t-turq" role="img" aria-label="Kitesurfer splashing in waves"></div><h3>Tittle goes here</h3><p>Pede Fusce tellus Sed metus augu</p><div class="price">$125.99</div></article>
    <article class="advert"><div class="photo t-ocean" role="img" aria-label="Open ocean horizon"></div><h3>Tittle goes here</h3><p>Pede Fusce tellus Sed metus augu</p><div class="price">$125.99</div></article>
    <article class="advert"><div class="photo t-sky" role="img" aria-label="Kites in a clear sky"></div><h3>Tittle goes here</h3><p>Pede Fusce tellus Sed metus augu</p><div class="price">$125.99</div></article>
    <article class="advert"><div class="photo t-sky" role="img" aria-label="Rider jumping under blue sky"></div><h3>Tittle goes here</h3><p>Pede Fusce tellus Sed metus augu</p><div class="price">$125.99</div></article>
  </div>
</section>

<section class="events">
  <h2 class="section-title">LATEST EVENTS</h2>
  <div class="wrap event-grid">
    <article class="event"><div class="photo t-beach" role="img" aria-label="Wide coastal beach view"></div><h3>Mauris vel lacus vitae</h3><p>Curabitur vel mi sit amet magna malesuada ultrices Ut nisi erat fermentum vel congue id euismod in elit Fusce ultricies orci</p></article>
    <article class="event"><div class="photo t-warm" role="img" aria-label="Rider holding board on the sand"></div><h3>Praesent elementum</h3><p>Curabitur vel mi sit amet magna malesuada ultrices Ut nisi erat fermen tum vel congue id euismod in elit Fusce ultricies orci</p></article>
    <article class="event"><div class="photo t-dark" role="img" aria-label="Portrait of an event speaker"></div><h3>Cum sociis natoque</h3><p>Curabitur vel mi sit amet magna malesuada ultrices Ut nisi erat fermen tum vel congue id euismod in elit Fusce ultricies orci</p></article>
    <article class="event"><div class="photo t-turq" role="img" aria-label="Kitesurfer riding a wave"></div><h3>Sed metus augue</h3><p>Curabitur vel mi sit amet magna malesuada ultrices Ut nisi erat fermentum vel congue id euismod in elit Fusce ultricies orci</p></article>
    <article class="event"><div class="photo t-sunset" role="img" aria-label="Kiteboarder jumping at golden sunset"></div><h3>Donec dictum</h3><p>Curabitur vel mi sit amet magna malesuada ultrices Ut nisi erat ferme ntum vel congue id euismod in elit Fusce ultricies orci</p></article>
  </div>
</section>

<section class="groups">
  <h2 class="section-title">LATEST GROUPS</h2>
  <div class="wrap group-grid">
    <article class="topic"><h3>Mauris vel lacus vitae</h3><div class="group-name">Group Name</div><p>Curabitur vel mi sit amet magna malesuada ultrices Ut nisi</p><div class="meta">By Author Name <span><svg width="12" height="10" viewBox="0 0 12 10"><path d="M7 0 L12 4.5 L7 9 V6 C4 6 2 7 0 10 C0.5 5.5 3 3 7 3Z" fill="#333a40"/></svg>Reply</span></div></article>
    <article class="topic"><h3>Mauris vel lacus vitae</h3><div class="group-name">Group Name</div><p>Curabitur vel mi sit amet magna malesuada ultrices Ut nisi</p><div class="meta">By Author Name <span><svg width="12" height="10" viewBox="0 0 12 10"><path d="M7 0 L12 4.5 L7 9 V6 C4 6 2 7 0 10 C0.5 5.5 3 3 7 3Z" fill="#333a40"/></svg>Reply</span></div></article>
    <article class="topic"><h3>Mauris vel lacus vitae</h3><div class="group-name">Group Name</div><p>Curabitur vel mi sit amet magna malesuada ultrices Ut nisi</p><div class="meta">By Author Name <span><svg width="12" height="10" viewBox="0 0 12 10"><path d="M7 0 L12 4.5 L7 9 V6 C4 6 2 7 0 10 C0.5 5.5 3 3 7 3Z" fill="#333a40"/></svg>Reply</span></div></article>
    <article class="topic"><h3>Mauris vel lacus vitae</h3><div class="group-name">Group Name</div><p>Curabitur vel mi sit amet magna malesuada ultrices Ut nisi</p><div class="meta">By Author Name <span><svg width="12" height="10" viewBox="0 0 12 10"><path d="M7 0 L12 4.5 L7 9 V6 C4 6 2 7 0 10 C0.5 5.5 3 3 7 3Z" fill="#333a40"/></svg>Reply</span></div></article>
    <article class="topic"><h3>Mauris vel lacus vitae</h3><div class="group-name">Group Name</div><p>Curabitur vel mi sit amet magna malesuada ultrices Ut nisi</p><div class="meta">By Author Name <span><svg width="12" height="10" viewBox="0 0 12 10"><path d="M7 0 L12 4.5 L7 9 V6 C4 6 2 7 0 10 C0.5 5.5 3 3 7 3Z" fill="#333a40"/></svg>Reply</span></div></article>

    <article class="topic"><h3>Mauris vel lacus vitae</h3><div class="group-name">Group Name</div><p>Curabitur vel mi sit amet magna malesuada ultrices Ut nisi</p><div class="meta">By Author Name <span><svg width="12" height="10" viewBox="0 0 12 10"><path d="M7 0 L12 4.5 L7 9 V6 C4 6 2 7 0 10 C0.5 5.5 3 3 7 3Z" fill="#333a40"/></svg>Reply</span></div></article>
    <article class="topic"><h3>Mauris vel lacus vitae</h3><div class="group-name">Group Name</div><p>Curabitur vel mi sit amet magna malesuada ultrices Ut nisi</p><div class="meta">By Author Name <span><svg width="12" height="10" viewBox="0 0 12 10"><path d="M7 0 L12 4.5 L7 9 V6 C4 6 2 7 0 10 C0.5 5.5 3 3 7 3Z" fill="#333a40"/></svg>Reply</span></div></article>
    <article class="topic"><h3>Mauris vel lacus vitae</h3><div class="group-name">Group Name</div><p>Curabitur vel mi sit amet magna malesuada ultrices Ut nisi</p><div class="meta">By Author Name <span><svg width="12" height="10" viewBox="0 0 12 10"><path d="M7 0 L12 4.5 L7 9 V6 C4 6 2 7 0 10 C0.5 5.5 3 3 7 3Z" fill="#333a40"/></svg>Reply</span></div></article>
    <article class="topic"><h3>Mauris vel lacus vitae</h3><div class="group-name">Group Name</div><p>Curabitur vel mi sit amet magna malesuada ultrices Ut nisi</p><div class="meta">By Author Name <span><svg width="12" height="10" viewBox="0 0 12 10"><path d="M7 0 L12 4.5 L7 9 V6 C4 6 2 7 0 10 C0.5 5.5 3 3 7 3Z" fill="#333a40"/></svg>Reply</span></div></article>
    <article class="topic"><h3>Mauris vel lacus vitae</h3><div class="group-name">Group Name</div><p>Curabitur vel mi sit amet magna malesuada ultrices Ut nisi</p><div class="meta">By Author Name <span><svg width="12" height="10" viewBox="0 0 12 10"><path d="M7 0 L12 4.5 L7 9 V6 C4 6 2 7 0 10 C0.5 5.5 3 3 7 3Z" fill="#333a40"/></svg>Reply</span></div></article>
  </div>
</section>

<section class="gallery">
  <svg class="notch" width="60" height="22" viewBox="0 0 60 22"><polygon points="0,0 60,0 30,22" fill="#ffffff"/></svg>
  <h2 class="section-title">PHOTO GALLERY</h2>
  <div class="wrap photo-grid">
    <div class="photo t-turq" role="img" aria-label="Windsurfer on turquoise sea"></div>
    <div class="photo t-sky" role="img" aria-label="Kitesurfer in spray"></div>
    <div class="photo t-warm" role="img" aria-label="Riders on the shore"></div>
    <div class="photo t-sky" role="img" aria-label="Rider gliding over waves"></div>
    <div class="photo t-sunset" role="img" aria-label="Kiteboarder silhouette at sunset"></div>

    <div class="photo t-turq" role="img" aria-label="Rider holding the kite bar"></div>
    <div class="photo t-sunset" role="img" aria-label="Jump against a yellow sky"></div>
    <div class="photo t-beach" role="img" aria-label="Kiteboarder leaning into the wind"></div>
    <div class="photo t-warm" role="img" aria-label="Rider on choppy water"></div>
    <div class="photo t-sky" role="img" aria-label="Kitesurfer mid-air"></div>

    <div class="photo t-turq" role="img" aria-label="Kites over a bright lagoon"></div>
    <div class="photo t-sky" role="img" aria-label="Rider splashing through surf"></div>
    <div class="photo t-turq" role="img" aria-label="Tropical shoreline with riders"></div>
    <div class="photo t-ocean" role="img" aria-label="Kitesurfer carving a wave"></div>
    <div class="photo t-sky" role="img" aria-label="Rider cruising on blue water"></div>
  </div>
</section>

<footer class="site-footer">
  <div class="wrap">
    <div>
      <nav class="footer-nav">
        <span>Home</span><span>|</span><span>How-To, Classifieds</span><span>|</span><span>Groups</span><span>|</span><span>News</span><span>|</span><span>Events</span><span>|</span><span>Contact us</span>
      </nav>
      <p class="copyright">© 2015 Company Name &nbsp;All right reserved &nbsp;Term of Use</p>
    </div>
    <div class="social"><span>tellora</span><span>chirpa</span><span>linkpro</span></div>
  </div>
</footer>

</body>
</html>
```